Maple Dawn Confections. We need a website as delcious as our chocolate.

I need a website to promote our humble chocolate business. We our proud of are chocolate because we use only our favorite ingredients. We believe in originality and complete enjoyment of our chocolates. I am looking for a sleek and smooth website. I would like to see typical pages such as contact information and an intro. I would like to have a product page, which can be easily updated with photos of new chocolate. I would also like to see a page where we can educate customers about chocolate. This might be tricky but I would like our customers to leave the site knowing they are getting great chocolate! I have a logo and general color scheme, which I will try to upload somewhere. I looking for an original and exciting website.
Updates

Websites we like:

1. http://www.corvel-amand.example/ (looks really good)

2. http://www.tilvarocacao.example/

uploaded logo !

Target Market(s)

People who enjoy chocolate.

Industry/Entity Type

Business

Requirements
Must have
• User Friendly
Page were pictures of new chocolate can be easily updated.

Nice to have
• Calming and appetizing music
Section where recent tweets can show up on the site.

```html
<!DOCTYPE html>
<html lang="en">
<head>
<meta charset="UTF-8">
<title>Maple Dawn Confections — Custom Gourmet Chocolates</title>
<link rel="stylesheet" href="https://fonts.googleapis.com/css2?family=Raleway:wght@200;300;400;500&family=Source+Sans+3:wght@400;600;700&family=Montserrat:wght@700&display=swap">
<style>
  :root {
    --magenta: #b43aa6;
    --cocoa-deep: #2a120b;
    --cocoa-mid: #5a2c1c;
    --caramel: #c9803c;
    --caramel-text: #d9903f;
    --ink: #3f2320;
    --cream: #ffffff;
    --footer-link: #efc6cf;
    --footer-text: #dcc4bb;
  }
  html, body {
    margin: 0;
    padding: 0;
    width: 1200px;
    height: 1080px;
    overflow: hidden;
    background: var(--cocoa-deep);
  }
  .canvas {
    position: relative;
    width: 1200px;
    height: 1080px;
    overflow: hidden;
    background: radial-gradient(ellipse at 30% 90%, #4a2216 0%, var(--cocoa-deep) 70%);
    font-family: "Source Sans 3", sans-serif;
  }
  .backdrop { position: absolute; inset: 0; }
  .brand {
    position: absolute;
    left: 42px;
    top: 62px;
    margin: 0;
    width: 260px;
    font-family: "Raleway", sans-serif;
    font-weight: 500;
    font-size: 30px;
    line-height: 1.15;
    color: var(--magenta);
  }
  .main-nav {
    position: absolute;
    left: 326px;
    top: 75px;
    display: flex;
    gap: 30px;
    font-family: "Raleway", sans-serif;
    font-weight: 400;
    font-size: 21px;
  }
  .main-nav a { color: var(--ink); text-decoration: none; }
  .hero-title {
    position: absolute;
    left: 50px;
    top: 196px;
    margin: 0;
    font-family: "Raleway", sans-serif;
    font-weight: 200;
    font-size: 80px;
    line-height: 62px;
    letter-spacing: -1.5px;
    color: var(--magenta);
  }
  .hero-title span { display: block; }
  .hero-title .indent { padding-left: 186px; }
  .hero-sub {
    position: absolute;
    left: 186px;
    top: 350px;
    margin: 0;
    font-family: "Raleway", sans-serif;
    font-weight: 300;
    font-size: 36px;
    line-height: 44px;
    letter-spacing: -0.5px;
    color: var(--ink);
  }
  .hero-sub span { display: block; }
  .hero-sub .indent { padding-left: 64px; }
  .badge {
    position: absolute;
    border-radius: 50%;
    color: var(--cream);
    text-align: center;
    display: flex;
    flex-direction: column;
    align-items: center;
    justify-content: center;
  }
  .badge-small {
    left: 503px; top: 510px; width: 88px; height: 88px;
    background: var(--caramel);
  }
  .badge-small .pct { font-size: 26px; font-weight: 600; line-height: 22px; letter-spacing: -1px; }
  .badge-small .off { font-size: 16px; font-weight: 600; line-height: 15px; }
  .badge-small .note { font-size: 10px; line-height: 10px; }
  .badge-large {
    left: 574px; top: 476px; width: 148px; height: 148px;
    background: var(--cocoa-mid);
  }
  .badge-large .pct { font-size: 48px; font-weight: 600; line-height: 40px; letter-spacing: -2px; margin-top: 6px; }
  .badge-large .off { font-size: 26px; font-weight: 600; line-height: 26px; }
  .badge-large .note { font-size: 15px; line-height: 18px; margin-top: 4px; }
  .intro {
    position: absolute;
    left: 746px;
    top: 514px;
    width: 384px;
    margin: 0;
    font-size: 15px;
    line-height: 21px;
    color: var(--cream);
    text-align: justify;
    text-align-last: justify;
  }
  .intro em { font-style: normal; color: var(--caramel-text); }
  .follow {
    position: absolute;
    left: 758px;
    top: 568px;
    display: flex;
    align-items: baseline;
    gap: 16px;
  }
  .follow-label { font-size: 15px; color: var(--caramel-text); letter-spacing: 0.3px; }
  .follow a {
    font-weight: 700;
    font-size: 22px;
    color: var(--cream);
    text-decoration: none;
  }
  .features {
    position: absolute;
    left: 68px;
    top: 650px;
    display: flex;
    gap: 20px;
  }
  .feature { width: 338px; }
  .feature-photo { display: block; width: 338px; height: 196px; }
  .photo-bonbons { background: radial-gradient(circle at 45% 40%, #8a4a30 0%, #6b2a3e 45%, #3a1510 100%); }
  .photo-bag { background: linear-gradient(120deg, #f6f3f6 0%, #e7dbea 45%, #6e3e2c 70%, #f4f1f4 100%); }
  .photo-box { background: linear-gradient(160deg, #f6f4f7 0%, #e8e0ec 35%, #5a2a26 60%, #7a2f3a 100%); }
  .feature h2 {
    margin: 12px 0 3px 0;
    font-family: "Raleway", sans-serif;
    font-weight: 400;
    font-size: 24px;
    letter-spacing: -0.3px;
    color: var(--caramel-text);
  }
  .feature p {
    margin: 0;
    font-size: 14px;
    line-height: 20px;
    color: var(--cream);
  }
  .footer-nav {
    position: absolute;
    left: 72px;
    top: 992px;
    display: flex;
    gap: 27px;
    font-family: "Montserrat", sans-serif;
    font-weight: 700;
    font-size: 12px;
    letter-spacing: 2.2px;
    text-transform: uppercase;
  }
  .footer-nav a { color: var(--footer-link); text-decoration: none; }
  .copyright {
    position: absolute;
    right: 80px;
    top: 989px;
    margin: 0;
    font-size: 15px;
    color: var(--footer-text);
  }
  .copyright a { color: var(--footer-text); text-decoration: none; }
</style>
</head>
<body>
<div class="canvas">
  <svg class="backdrop" width="1200" height="1080" viewBox="0 0 1200 1080">
    <defs>
      <linearGradient id="pinkFade" x1="0" y1="0" x2="1" y2="0.3">
        <stop offset="0" stop-color="#f4c0d2"/>
        <stop offset="0.6" stop-color="#f8d2df"/>
        <stop offset="1" stop-color="#fbe1ea"/>
      </linearGradient>
      <radialGradient id="bonbonTones" cx="0.6" cy="0.45" r="0.7">
        <stop offset="0" stop-color="#8c4a2e"/>
        <stop offset="0.45" stop-color="#6e2a44"/>
        <stop offset="1" stop-color="#3e1812"/>
      </radialGradient>
      <linearGradient id="caramelBand" x1="0" y1="0" x2="1" y2="0">
        <stop offset="0" stop-color="#c97a34"/>
        <stop offset="0.6" stop-color="#a85e2c"/>
        <stop offset="1" stop-color="#6a3420"/>
      </linearGradient>
    </defs>
    <path d="M0 0 L1200 0 L1200 470 L720 480 C640 560 520 610 420 606 C300 600 120 530 0 490 Z"
          fill="url(#pinkFade)"/>
    <path role="img" aria-label="Photo of assorted gourmet chocolates in purple paper cups"
          d="M1000 0 L1200 0 L1200 500 C1080 470 900 470 720 492 C690 420 700 300 760 200 C820 110 900 40 1000 0 Z"
          fill="url(#bonbonTones)"/>
    <path d="M0 490 C120 530 300 600 420 606 C520 610 640 560 720 480 C660 580 560 640 440 640 C320 640 140 610 0 610 Z"
          fill="url(#caramelBand)"/>
  </svg>

  <h1 class="brand">Maple Dawn Confections</h1>

  <nav class="main-nav">
    <a href="#">Home</a>
    <a href="#">About Maple Dawn</a>
    <a href="#">Products</a>
    <a href="#">Contact Us</a>
  </nav>

  <h2 class="hero-title"><span>Make a Sweet</span><span class="indent">Impression</span></h2>
  <p class="hero-sub"><span>With Our Custom</span><span class="indent">Gourmet Chocolates</span></p>

  <div class="badge badge-small"><span class="pct">10%</span><span class="off">OFF</span><span class="note">Introductory<br>Offer</span></div>
  <div class="badge badge-large"><span class="pct">25%</span><span class="off">OFF</span><span class="note">Introductory<br>Offer</span></div>

  <p class="intro">Lorem ipsum dolor sit amet, consectetuer adipiscing elit, sed diam nonummy nibh euismod <em>tincidunt ut laoreet</em> dolore</p>

  <div class="follow">
    <span class="follow-label">FOLLOW US ON:</span>
    <a href="#">Chatterline</a>
    <a href="#">Friendwall</a>
  </div>

  <section class="features">
    <article class="feature">
      <div class="feature-photo photo-bonbons" role="img" aria-label="Close-up photo of chocolate bonbons in paper cups"></div>
      <h2>Special Introductory Offer!</h2>
      <p>Lorem ipsum dolor sit amet, consectetuer adipiscing elit, sed diam nonummy nibh euismod tincidunt.</p>
    </article>
    <article class="feature">
      <div class="feature-photo photo-bag" role="img" aria-label="Photo of a gift bag beside an open box of assorted chocolates"></div>
      <h2>A wide selection and a variety</h2>
      <p>Lorem ipsum dolor sit amet, consectetuer adipiscing elit, sed diam nonummy nibh euismod tincidunt.</p>
    </article>
    <article class="feature">
      <div class="feature-photo photo-box" role="img" aria-label="Photo of an open presentation box filled with chocolates"></div>
      <h2>Personalized your Order</h2>
      <p>Lorem ipsum dolor sit amet, consectetuer adipiscing elit, sed diam nonummy nibh euismod tincidunt.</p>
    </article>
  </section>

  <nav class="footer-nav">
    <a href="#">Home</a>
    <a href="#">About Maple Dawn</a>
    <a href="#">Products</a>
    <a href="#">Contact Us</a>
  </nav>
  <p class="copyright">Copyright © Maple Dawn Confections | <a href="#">Privacy Policy</a> | <a href="#">Contact Us</a></p>
</div>
</body>
</html>
```